I need a business card design for a new company that will be doing consulting work around issues of cultural competency, and diversity and inclusion. I would like the design to be crisp and clear with bold but conservative colors and incorporate shades of blue

Target Market(s)

Small businesses, schools, non-profits

Industry/Entity Type

Consulting

Font styles to use
Serif
Sans Serif

Colors
0c5ba6
6b449b
3276b5
0292cd

Requirements
Must have
• A Morrow Venture (name of company)
• Lemlem Tavish
• CEO
• lemlem@amorrowventure.com
• (215)483-2756

```html
<!DOCTYPE html>
<html lang="en">
<head>
<meta charset="utf-8">
<title>Lemlem Tavish – Business Card</title>
<link href="https://fonts.googleapis.com/css2?family=Lato:wght@400;700;900&family=Nunito+Sans:wght@400&display=swap" rel="stylesheet">
<style>
  :root {
    --backdrop: #dfe2e6;
    --card: #ffffff;
    --brand-blue: #0c6cbf;
    --ink: #1d1d1f;
    --rule: #2a2a2a;
  }
  * { margin: 0; padding: 0; box-sizing: border-box; }
  html, body {
    width: 1200px;
    height: 1015px;
    overflow: hidden;
    background: var(--backdrop);
  }
  .business-card {
    position: absolute;
    left: 75px;
    top: 207px;
    width: 1050px;
    height: 600px;
    background: var(--card);
    box-shadow: 0 6px 24px rgba(0,0,0,0.12);
    overflow: hidden;
  }
  .accent-band {
    position: absolute;
    left: 0;
    bottom: 0;
    width: 100%;
    height: 16px;
    background: var(--brand-blue);
  }
  .identity {
    position: absolute;
    left: 200px;
    top: 228px;
    width: 650px;
  }
  .name-row {
    display: flex;
    align-items: baseline;
    padding-left: 130px;
    margin-bottom: 10px;
    white-space: nowrap;
  }
  .person-name {
    font-family: "Lato", sans-serif;
    font-size: 40px;
    color: var(--brand-blue);
    letter-spacing: 1px;
    font-weight: 400;
  }
  .person-name .surname { font-weight: 900; }
  .job-title {
    font-family: "Lato", sans-serif;
    font-size: 22px;
    color: var(--ink);
    margin-left: 16px;
    letter-spacing: 1px;
  }
  .contact-row {
    display: flex;
    border-top: 2px solid var(--rule);
  }
  .contact-item {
    display: flex;
    align-items: center;
    gap: 10px;
    font-family: "Nunito Sans", sans-serif;
    font-size: 21px;
    color: var(--ink);
    padding-top: 12px;
    white-space: nowrap;
    flex: none;
  }
  .contact-phone {
    width: 280px;
    padding-left: 50px;
  }
  .contact-divider {
    flex: none;
    width: 2px;
    height: 44px;
    background: var(--rule);
    margin-right: 22px;
  }
  .contact-icon { width: 24px; height: 20px; flex: none; }
</style>
</head>
<body>
  <main class="business-card">
    <section class="identity">
      <div class="name-row">
        <h1 class="person-name">LEMLEM <span class="surname">TAVISH</span></h1>
        <span class="job-title">CEO</span>
      </div>
      <div class="contact-row">
        <div class="contact-item contact-phone">
          <svg class="contact-icon" viewBox="0 0 24 20" aria-hidden="true">
            <path d="M1 7 C4 2 20 2 23 7 L20 9 L17 6.5 L7 6.5 L4 9 Z" fill="#0c6cbf"/>
            <path d="M6 9 L18 9 L21 18 L3 18 Z" fill="#0c6cbf"/>
            <circle cx="12" cy="13.5" r="2.6" fill="#fff"/>
          </svg>
          <span>(215)483-2756</span>
        </div>
        <div class="contact-divider"></div>
        <div class="contact-item contact-email">
          <svg class="contact-icon" viewBox="0 0 24 18" aria-hidden="true">
            <rect x="0" y="1" width="24" height="16" fill="#0c6cbf"/>
            <path d="M1 2 L12 10 L23 2" fill="none" stroke="#fff" stroke-width="1.6"/>
            <path d="M1 16 L9 8.5 M23 16 L15 8.5" fill="none" stroke="#fff" stroke-width="1.4"/>
          </svg>
          <span>lemlem@amorrowventure.com</span>
        </div>
      </div>
    </section>
    <div class="accent-band"></div>
  </main>
</body>
</html>
```